Torvel Business Cards

Business card design. dont mind if new logo is suggested.
it would be for a security company.
our clients would be bigger security companies around Australia.
have a logo done but can be replaced. see attaached. like the colors.
Need company name, person name, designation, phone and email on front.
At back company logo and name. website saddress and 2 x license numbers
would like to have 2 different background color for both sidde

Industry/Entity Type

Security

Contact Information for Business Card

round corners, front should be light in color. need logo at back with webaddress and 2 x license numners

Font styles to use
Sans Serif

Colors
f37122
faa54b
f8ba93
0255a3
0592cd
85cae6
b3d448
9bcb3c
ffffff

Requirements
Must have
• see description
Nice to have
• see description
Should not have
• should not be difficult to read or hardd to find information on card.. lets say easy on eyes yet catchy

```html
<!DOCTYPE html>
<html lang="en">
<head>
<meta charset="utf-8">
<title>Torvel Security Group – Business Cards</title>
<link rel="stylesheet" href="https://fonts.googleapis.com/css2?family=Marcellus&family=Open+Sans:wght@400;600;700&display=swap">
<style>
  :root {
    --stage: #2b2b2b;
    --paper: #f4f4f2;
    --navy: #0b3a6e;
    --sky: #1aa6c8;
    --sky-light: #8fd3e6;
    --grey: #6a6a6a;
    --teal-a: #19d3e0;
    --teal-b: #0590b4;
    --white: #ffffff;
  }
  * { box-sizing: border-box; margin: 0; padding: 0; }
  html, body {
    width: 1200px; height: 900px; overflow: hidden;
    background: var(--stage);
  }
  .canvas { position: relative; width: 1200px; height: 900px; }

  .card {
    position: absolute;
    border-radius: 14px;
    overflow: hidden;
    box-shadow: 0 12px 30px rgba(0,0,0,.45);
  }

  /* Back side */
  .card-back {
    left: 70px; top: 280px; width: 595px; height: 340px;
    background: linear-gradient(100deg, var(--teal-a) 0%, var(--teal-b) 100%);
    color: var(--white);
  }
  .back-brand {
    position: absolute; left: 0; right: 0; top: 108px;
    display: flex; flex-direction: column; align-items: center;
  }
  .brand-mark {
    width: 46px; height: 46px; border-radius: 50%;
    background: var(--white); margin-bottom: 14px;
  }
  .back-name {
    font-family: "Marcellus", serif;
    font-size: 25px; letter-spacing: 1px; text-transform: uppercase;
  }
  .back-web {
    font-family: "Open Sans", sans-serif;
    font-size: 13px; letter-spacing: 6px; margin-top: 4px;
  }
  .back-licences {
    position: absolute; left: 0; right: 0; bottom: 46px; text-align: center;
    font-family: "Open Sans", sans-serif; font-size: 14px;
  }
  .back-licences .divider { margin: 0 10px; }

  /* Front side */
  .card-front {
    left: 770px; top: 150px; width: 340px; height: 595px;
    background: var(--paper);
  }
  .front-brand {
    position: absolute; top: 48px; left: 0; right: 0;
    display: flex; align-items: center; justify-content: center; gap: 12px;
  }
  .front-brand .brand-mark { width: 26px; height: 26px; margin: 0; background: var(--sky); }
  .front-name {
    font-family: "Marcellus", serif; color: var(--navy);
    font-size: 20px; letter-spacing: .5px; text-transform: uppercase;
  }
  .contact-ring {
    position: absolute; left: 30px; top: 210px; width: 280px; height: 280px;
  }
  .contact {
    position: absolute; left: 90px; top: 290px;
    font-family: "Open Sans", sans-serif; color: var(--grey);
    font-size: 13px; line-height: 1.5;
  }
  .person {
    font-weight: 700; color: var(--navy); font-size: 17px; text-transform: uppercase;
  }
  .role {
    color: var(--sky); font-size: 14px; text-transform: uppercase; margin-bottom: 6px;
  }
</style>
</head>
<body>
<main class="canvas">

  <section class="card card-back" aria-label="Card back">
    <div class="back-brand">
      <span class="brand-mark"></span>
      <div class="back-name">Torvel Security Group</div>
      <div class="back-web">www.torvelgroup.com</div>
    </div>
    <div class="back-licences">Lic No. #40817236<span class="divider">|</span>#73520914</div>
  </section>

  <section class="card card-front" aria-label="Card front">
    <div class="front-brand">
      <span class="brand-mark"></span>
      <span class="front-name">Torvel Security Group</span>
    </div>

    <svg class="contact-ring" viewBox="0 0 280 280" aria-hidden="true">
      <circle cx="140" cy="140" r="130" fill="none" stroke="var(--sky-light)" stroke-width="3"/>
    </svg>

    <div class="contact">
      <div class="person">Liam Archer</div>
      <div class="role">CEO/Founder</div>
      <div>412 Kestrel Way</div>
      <div>Ballarat, Victoria 3350</div>
      <div>613 482 7091</div>
      <div>liam@torvelgroup.com</div>
      <div>www.torvelgroup.com</div>
    </div>
  </section>

</main>
</body>
</html>
```